ALL TYPES OF COMMERCIAL PLASTERING

TYPE OF BLOCK LETTERING WITH STAND OUT QUALITIES
WITH SOME TYPE OF LOGO
SOMETHING UNIQUE FOR THE BUILDING INDUSTRY.
QUALITY WORKMANSHIP
Updates

forgot to include my mobile phone number on my brief. could you add it to your design please MOBILE PH 0418 695 031

please let me make this quite clear ,the company name is northgate linings and Fitouts PTY LTD. THE TYPE OF WORK WE WILL BE DOING IS COMMERCIAL PLASTERING.

Industry/Entity Type

Industry

Contact Information for Business Card

northgate linings and fitouts P/L
martin corbell p.o.box 42 wendouree 3355 email address northgatelinings@mailbox-example.com
ABN 51 847 213 906 COMMERCIAL PLASTERING

```html
<!DOCTYPE html>
<html lang="en">
<head>
<meta charset="utf-8">
<title>Northgate Linings and Fitouts – Business Card</title>
<link href="https://fonts.googleapis.com/css2?family=Oswald:wght@600&family=Open+Sans:wght@300;400;700&display=swap" rel="stylesheet">
<style>
  :root {
    --backdrop: #e9e6e1;
    --card-white: #ffffff;
    --card-shade: #f1f1f1;
    --band-dark: #1f2021;
    --band-mid: #3a3b3d;
    --accent: #ef6a2a;
    --accent-light: #f7a066;
    --ink: #262626;
    --ink-soft: #5a5a5a;
    --ink-faint: #a3a3a3;
    --on-dark: #ffffff;
  }
  * { margin: 0; padding: 0; box-sizing: border-box; }
  html, body { width: 1200px; height: 1023px; overflow: hidden; }
  body {
    background: var(--backdrop);
    font-family: "Open Sans", Arial, sans-serif;
    position: relative;
  }
  .business-card {
    position: absolute;
    left: 150px; top: 252px;
    width: 900px; height: 520px;
    border-radius: 26px;
    overflow: hidden;
    background: linear-gradient(160deg, var(--card-white) 55%, var(--card-shade));
    box-shadow: 0 18px 40px rgba(0,0,0,.25);
  }
  .card-band { position: absolute; inset: 0; width: 900px; height: 520px; }
  .brand {
    position: absolute; left: 54px; top: 50px;
    display: flex; align-items: center; gap: 22px;
  }
  .brand-mark {
    width: 86px; height: 86px; border-radius: 50%;
    background: var(--accent);
    flex: none;
  }
  .brand-name {
    font-family: "Oswald", "Arial Narrow", sans-serif;
    font-weight: 600;
    font-size: 38px; line-height: 1.05;
    color: var(--ink);
    text-transform: uppercase;
    letter-spacing: .5px;
  }
  .tagline {
    position: absolute; left: 56px; top: 162px;
    font-weight: 300; font-size: 22px;
    letter-spacing: 1.5px; color: var(--ink-soft);
    text-transform: uppercase;
  }
  .holder { position: absolute; left: 56px; top: 212px; }
  .holder-name {
    font-weight: 700; font-size: 30px;
    color: var(--accent); text-transform: uppercase; letter-spacing: .5px;
  }
  .holder-role { font-size: 19px; color: var(--ink-soft); margin-top: 2px; }
  .abn {
    position: absolute; right: 40px; top: 28px;
    font-size: 16px; color: var(--ink-faint);
  }
  .contact-list {
    position: absolute; right: 40px; top: 322px;
    list-style: none; text-align: right;
  }
  .contact-item {
    display: flex; justify-content: flex-end; align-items: center; gap: 12px;
    color: var(--on-dark); font-size: 19px; line-height: 38px;
  }
  .contact-item.address {
    color: var(--accent); font-weight: 700; text-transform: uppercase;
  }
  .contact-icon { width: 22px; height: 22px; flex: none; }
  .contact-icon.blank { visibility: hidden; }
</style>
</head>
<body>
  <div class="business-card">
    <svg class="card-band" viewBox="0 0 900 520" aria-hidden="true">
      <defs>
        <linearGradient id="bandShade" x1="0" y1="0" x2="1" y2="1">
          <stop offset="0" stop-color="var(--band-mid)"/>
          <stop offset="0.5" stop-color="var(--band-dark)"/>
          <stop offset="1" stop-color="var(--band-dark)"/>
        </linearGradient>
        <linearGradient id="stripeShade" x1="0" y1="1" x2="1" y2="0">
          <stop offset="0" stop-color="var(--accent)"/>
          <stop offset="1" stop-color="var(--accent-light)"/>
        </linearGradient>
      </defs>
      <path d="M684 0 C 544 200, 414 380, 284 520 L 900 520 L 900 0 Z" fill="url(#stripeShade)"/>
      <path d="M700 0 C 560 202, 432 382, 304 520 L 900 520 L 900 0 Z" fill="url(#bandShade)"/>
    </svg>

    <div class="brand">
      <span class="brand-mark"></span>
      <div class="brand-name">Northgate Linings<br>&amp; Fitouts PTY LTD</div>
    </div>
    <p class="tagline">Specialists in commercial plastering</p>
    <div class="holder">
      <p class="holder-name">Martin Corbell</p>
      <p class="holder-role">Director</p>
    </div>
    <p class="abn">ABN 51 847 213 906</p>

    <ul class="contact-list">
      <li class="contact-item">0418 695 031
        <svg class="contact-icon" viewBox="0 0 22 22" aria-hidden="true"><rect width="22" height="22" rx="3" fill="var(--accent)"/><rect x="7" y="4" width="8" height="14" rx="1.5" fill="none" stroke="#fff" stroke-width="1.6"/></svg>
      </li>
      <li class="contact-item">0353 210 468
        <svg class="contact-icon" viewBox="0 0 22 22" aria-hidden="true"><rect width="22" height="22" rx="3" fill="var(--accent)"/><path d="M6 5 L9 5 L10 9 L8.5 10.5 C9.5 12.5 10.5 13.5 12.5 14.5 L14 13 L18 14 L18 17 C11 17.5 5 11 6 5 Z" fill="#fff"/></svg>
      </li>
      <li class="contact-item">northgatelinings@mailbox-example.com
        <svg class="contact-icon" viewBox="0 0 22 22" aria-hidden="true"><rect width="22" height="22" rx="3" fill="var(--accent)"/><rect x="4" y="6" width="14" height="10" fill="none" stroke="#fff" stroke-width="1.6"/><path d="M4 6 L11 12 L18 6" fill="none" stroke="#fff" stroke-width="1.6"/></svg>
      </li>
      <li class="contact-item address">P.O.Box 42 Wendouree 3355
        <svg class="contact-icon blank" viewBox="0 0 22 22" aria-hidden="true"></svg>
      </li>
    </ul>
  </div>
</body>
</html>
```